Anwaltskanzlei sucht Design für Geschäftspapier, Visitenkarten, Marketing unter Einbindung des neuen Logos
Zielgruppe
Anwaltliche Rechtsberatung und Rechtsvertretung auf den Gebieten des Arbeits-, Gesellschafts- und Wirtschaftsrechts sowie des Datenschutzrechts
Zielgruppe: Mittelständische Unternehmen aller Rechtsformen und Branchen
In Kooperation mit Kanzlei Velbrand (www.kanzlei-velbrand.de)
Inhaber einer weiteren Kanzlei Velbrand & Krüger
Aufgabenstellung
Einbindung des übersandten Logos
ggf. Slogan: Kanzlei für den Mittelstand
optional: Nennung der Rechtsgebiete

```html
<!DOCTYPE html>
<html lang="de">
<head>
<meta charset="utf-8">
<title>Anwaltskanzlei Hossmer – Visitenkarte</title>
<link href="https://fonts.googleapis.com/css2?family=Montserrat:wght@400;500;700&display=swap" rel="stylesheet">
<style>
  :root {
    --navy: #212c4d;
    --silver: #b9b8bd;
    --muted: #8c8c8c;
    --paper: #ffffff;
    --backdrop: #e4e5ea;
  }
  * { margin: 0; padding: 0; box-sizing: border-box; }
  html, body {
    width: 1200px; height: 720px; overflow: hidden;
    background: var(--backdrop);
    font-family: "Montserrat", sans-serif;
  }
  .card {
    position: absolute; top: 178px;
    width: 510px; height: 331px;
    background: var(--paper);
    overflow: hidden;
  }
  .card--front { left: 85px; }
  .card--back { left: 637px; }

  .front-panel { position: absolute; inset: 0; width: 100%; height: 100%; }

  .firm-name {
    position: absolute; left: 56px; top: 32px;
    color: var(--silver);
    font-size: 11px; font-weight: 500; line-height: 1.1;
    letter-spacing: 0.2px; text-transform: uppercase;
    white-space: nowrap;
  }
  .person {
    position: absolute; left: 263px; width: 240px; top: 66px;
    text-align: center; white-space: nowrap;
  }
  .person__name { color: var(--navy); font-size: 21px; font-weight: 700; line-height: 26px; }
  .person__role { color: var(--muted); font-size: 16px; font-weight: 400; line-height: 20px; margin-top: 6px; }

  .contact { position: absolute; color: var(--navy); font-size: 13px; font-weight: 500; line-height: 16px; white-space: nowrap; }
  .contact svg { position: absolute; fill: var(--navy); }
  .contact--phone { left: 284px; top: 187px; }
  .contact--phone svg { left: -27px; top: 0; }
  .contact--mail { left: 303px; top: 215px; }
  .contact--mail svg { left: -30px; top: 2px; }
  .contact--address { left: 320px; top: 243px; }
  .contact--address svg { left: -21px; top: 8px; }

  .brand-square {
    position: absolute; left: 197px; top: 110px;
    width: 115px; height: 111px;
    background: var(--navy); border-radius: 5px;
    display: flex; align-items: center; justify-content: center;
    text-align: center; padding: 0 8px;
    color: var(--silver); font-size: 9px; font-weight: 500;
    line-height: 1.35; text-transform: uppercase; letter-spacing: 0;
    white-space: nowrap;
  }
  .slogan {
    position: absolute; left: 0; right: 0; top: 240px;
    text-align: center; color: var(--muted);
    font-size: 17px; font-weight: 400; white-space: nowrap;
  }
</style>
</head>
<body>
  <section class="card card--front">
    <svg class="front-panel" viewBox="0 0 510 331" aria-hidden="true">
      <polygon points="0,0 185,0 82,331 0,331" fill="var(--navy)"/>
      <polygon points="185,0 215,0 112,331 82,331" fill="var(--silver)"/>
    </svg>
    <p class="firm-name">Anwaltskanzlei<br>Hossmer</p>

    <div class="person">
      <p class="person__name">Name Surname</p>
      <p class="person__role">Lawyer</p>
    </div>

    <p class="contact contact--phone">
      <svg width="15" height="15" viewBox="0 0 24 24" aria-hidden="true"><path d="M6.6 10.8a15.1 15.1 0 0 0 6.6 6.6l2.2-2.2c.3-.3.7-.4 1-.2 1.1.4 2.3.6 3.6.6.6 0 1 .4 1 1V20c0 .6-.4 1-1 1C10.6 21 3 13.4 3 4c0-.6.4-1 1-1h3.5c.6 0 1 .4 1 1 0 1.3.2 2.5.6 3.6.1.3 0 .7-.2 1z"/></svg>
      +49 (0) 12345678910
    </p>
    <p class="contact contact--mail">
      <svg width="17" height="12" viewBox="0 0 17 12" aria-hidden="true"><rect x="0" y="0" width="17" height="12" rx="1.5"/><path d="M2 2l6.5 5L15 2M2 10l4-3.5M15 10l-4-3.5" stroke="#fff" stroke-width="1.1" fill="none"/></svg>
      N.Surname@firm.de
    </p>
    <p class="contact contact--address">
      <svg width="13" height="16" viewBox="0 0 13 16" aria-hidden="true"><path d="M6.5 0A6.5 6.5 0 0 0 0 6.5C0 11 6.5 16 6.5 16S13 11 13 6.5A6.5 6.5 0 0 0 6.5 0z"/><circle cx="6.5" cy="6.3" r="2.2" fill="#fff"/><circle cx="6.5" cy="6.3" r="1.2"/></svg>
      123 Av. ABCD City<br>Germany
    </p>
  </section>

  <section class="card card--back">
    <div class="brand-square">Anwaltskanzlei<br>Hossmer</div>
    <p class="slogan">Kanzlei für den Mittelstand</p>
  </section>
</body>
</html>
```